Business Card Design

We are starting up a new Family run Business mainly offering a Free House Clearance service. We also offer the following chargeable services which include a Removals Service, Delivery and Collection of Items sold or purchased on Bidloft, Swapcorner etc, including Motorcycles, Piano's, Furniture, Electrical appliances.
As there are a few Companies offering similar services we need to stand out and show what we do at a glance while appearing Professional and approachable
Updates

TidyNests

i  am liking some of the colours and designs so far but would like to see a few of our services listed as 1 or 2 have already done if this is possible and maybe some emphasis on the FREE House Clearance. thank you 
best regards
derek

Target Market(s)

Commercial and Domestic Tenants and Landlords aswell as Families looking for a friendly sympathetic clearance service after bereavement

Industry/Entity Type

Business

Contact Information for Business Card

TidyNests,
HouseClearance and Removals,
Brynmor Vale
CF47 2RL
Tel: 07831562904
Email: enquiries@tidynests.example

```html
<!DOCTYPE html>
<html lang="en">
<head>
<meta charset="utf-8">
<title>TidyNests – Business Card</title>
<link rel="stylesheet" href="https://fonts.googleapis.com/css2?family=Alegreya+Sans+SC:wght@700;800&family=Questrial&display=swap">
<style>
  :root {
    --backdrop: #d3cdcf;
    --navy-deep: #262c5c;
    --navy-mid: #3a4589;
    --navy-glow: #4a56a0;
    --cyan-accent: #5fc3d8;
    --paper: #ffffff;
    --ink: #1e1e24;
    --yellow-top: #ffef5a;
    --yellow-bottom: #f2cf1b;
    --badge-ink: #262c5c;
  }
  * { box-sizing: border-box; margin: 0; padding: 0; }
  html, body {
    width: 1200px;
    height: 845px;
    overflow: hidden;
    background: var(--backdrop);
  }
  .canvas {
    position: relative;
    width: 1200px;
    height: 845px;
  }
  .card {
    position: absolute;
    top: 282px;
    width: 480px;
    height: 280px;
    overflow: hidden;
    box-shadow: 0 6px 18px rgba(40, 30, 45, 0.18);
  }
  .card--front {
    left: 90px;
    background: radial-gradient(ellipse 70% 60% at 50% 55%, var(--navy-glow) 0%, var(--navy-mid) 45%, var(--navy-deep) 100%);
    display: flex;
    flex-direction: column;
    align-items: center;
    justify-content: center;
  }
  .front-title {
    font-family: "Alegreya Sans SC", sans-serif;
    font-weight: 800;
    font-size: 40px;
    letter-spacing: 0.5px;
    color: var(--paper);
    line-height: 1;
  }
  .front-tagline {
    font-family: "Questrial", sans-serif;
    font-size: 17px;
    color: var(--cyan-accent);
    letter-spacing: 0.5px;
    margin-top: 2px;
  }
  .card--back {
    left: 630px;
    background: var(--paper);
  }
  .back-band {
    position: absolute;
    left: 0; top: 0;
    width: 100%;
    height: 142px;
    background: radial-gradient(ellipse 70% 80% at 50% 70%, var(--navy-glow) 0%, var(--navy-mid) 50%, var(--navy-deep) 100%);
    text-align: center;
    color: var(--paper);
    font-family: "Alegreya Sans SC", sans-serif;
    font-weight: 700;
  }
  .company-name {
    font-size: 19px;
    padding-top: 48px;
    line-height: 1;
  }
  .company-services {
    font-size: 19px;
    margin-top: 16px;
    line-height: 1;
  }
  .location-badge {
    position: absolute;
    left: 240px;
    top: 118px;
    width: 178px;
    height: 46px;
    border-radius: 5px;
    background: linear-gradient(to bottom, var(--yellow-top), var(--yellow-bottom));
    text-align: center;
    color: var(--badge-ink);
    font-family: "Alegreya Sans SC", sans-serif;
    font-weight: 800;
  }
  .location-town {
    font-size: 20px;
    line-height: 1;
    padding-top: 6px;
  }
  .location-postcode {
    font-size: 11px;
    line-height: 1;
    margin-top: 1px;
  }
  .contact-list {
    position: absolute;
    left: 0;
    top: 176px;
    width: 100%;
    list-style: none;
    text-align: center;
    font-family: "Questrial", sans-serif;
    color: var(--ink);
  }
  .contact-phone {
    font-size: 26px;
    line-height: 1.3;
    padding-left: 60px;
  }
  .contact-email {
    font-size: 24px;
    line-height: 1.4;
  }
</style>
</head>
<body>
  <main class="canvas">
    <section class="card card--front" aria-label="Card front">
      <h1 class="front-title">Free House Clearance</h1>
      <p class="front-tagline">service</p>
    </section>

    <section class="card card--back" aria-label="Card back">
      <div class="back-band">
        <p class="company-name">TidyNests</p>
        <p class="company-services">HouseClearance and Removals</p>
      </div>
      <div class="location-badge">
        <p class="location-town">Brynmor Vale</p>
        <p class="location-postcode">CF47 2RL</p>
      </div>
      <ul class="contact-list">
        <li class="contact-phone">T: 07831562904</li>
        <li class="contact-email">E: enquiries@tidynests.example</li>
      </ul>
    </section>
  </main>
</body>
</html>
```